Website for Public Relations Agency called "Tall Pine"

A need a website for a new business which is essentially a Public Relations/ Marketing business. We offer services to small family businesses, medium enterprise as well as multinational companies (ie we sell our professional services to other businesses; we are not a consumer brand).
The website needs to be polished, professional and modern. Because of the services we offer, I really need the website to be a little bit "wow".
Colours - we have a logo (see files) so the colour palette for the website should be dictated by this.
The Word doc attached mapped out the various pages that will make up the site. The text is not 100% finalised but it's good enough to give you a good picture of what the site will talk about.
I am not selling directly off my site, so this is an informational site only to explain who i am and what i do.
Target Market(s)
Other businesses - small family business, medium business and large multinational companies
Industry/Entity Type
Marketing
Coding
Coded - Design and coding required
Number of Pages Required
5+ page
Requirements
Must have
- Given my business, really looking for a little "wow" factor on the home page
Should not have
- I don't know if this is relevant to the coding, but I want to end up on a platform that I can myself make copy/ text edits as I please. I do not want to have to go through a deisgn company for small text changes in 6 or 12 months time.

```html
<!DOCTYPE html>
<html lang="en">
<head>
<meta charset="utf-8">
<title>Tall Pine | Strategic Communication</title>
<link href="https://fonts.googleapis.com/css2?family=Poppins:wght@300;400;500;600;700&display=swap" rel="stylesheet">
<style>
:root{
  --pink:#e3428f;
  --purple:#6b3fa0;
  --ink:#1d1d1f;
  --muted:#555;
  --blush:#fbeaf3;
  --blush-deep:#f6d4e4;
  --white:#fff;
}
*{box-sizing:border-box;margin:0;padding:0}
html,body{width:1200px;height:4554px;overflow:hidden}
body{font-family:'Poppins',sans-serif;color:var(--ink);background:var(--white);position:relative}
.sec{position:absolute;left:0;width:1200px}
.abs{position:absolute}
.accent{color:var(--pink);font-weight:600}
.h2{font-size:45px;font-weight:300;line-height:1.1}
.h2 .accent{font-weight:600}
.btn{position:absolute;display:flex;align-items:center;justify-content:center;border-radius:30px;font-size:16px;font-weight:500;background:var(--purple);color:#fff;box-shadow:0 4px 10px rgba(107,63,160,.3)}
.btn-outline{background:#fff;color:var(--purple);border:1.5px solid var(--purple);box-shadow:none}

/* nav */
.nav{top:0;height:92px;background:#fff}
.brand{position:absolute;display:flex;align-items:center;gap:10px;font-weight:500;color:var(--pink)}
.brand-mark{width:26px;height:26px;border:2px solid var(--purple);border-radius:4px}
.nav .brand{left:64px;top:28px;font-size:28px}
.menu{position:absolute;left:526px;top:30px;display:flex;gap:16px;font-size:16px}
.menu span{padding:4px 14px}
.menu .on{background:var(--pink);color:#fff;border-radius:2px}
.nav .btn{left:951px;top:20px;width:188px;height:52px}

/* hero */
.hero{top:92px;height:583px;background:linear-gradient(90deg,#fbeaf2 0%,#f6e4f0 60%,#efe0f2 100%)}
.hero h1{left:60px;top:96px;font-size:57px;line-height:1.05;font-weight:300}
.hero h1 b{font-weight:700}
.hero h1 .accent{font-weight:300}
.hero h1 b .accent{font-weight:700}
.hero .sub{left:60px;top:246px;font-size:17px;font-weight:600}
.hero .lead{left:60px;top:298px;width:560px;font-size:17px;line-height:1.45}
.hero .can{left:60px;top:368px;font-size:17px}
.hero .btn{left:60px;top:430px;width:262px;height:56px}
.hero-photo{left:640px;top:0;width:560px;height:583px;background:radial-gradient(ellipse 45% 55% at 62% 50%,#6aa8e8 0%,#8d7fd8 40%,#d9c9ef 75%,rgba(246,228,240,0) 100%)}

/* marketing */
.mkt{top:675px;height:944px;background:#fff}
.mkt .h2{left:60px;top:58px}
.mkt .intro{left:60px;top:186px;font-size:16px}
.card{position:absolute;width:338px;height:227px;background:#fff;box-shadow:0 2px 8px rgba(0,0,0,.14);padding:24px 26px}
.ico{width:54px;height:54px;border:2px solid var(--pink);border-radius:6px;margin-bottom:18px;position:relative}
.ico::after{content:"";position:absolute;left:12px;top:12px;width:26px;height:26px;border:2px solid var(--purple);border-radius:50%}
.card h3{font-size:18px;font-weight:500;margin-bottom:14px}
.card p{font-size:14px;line-height:1.3;color:var(--muted)}
.mkt .close{left:300px;top:772px;width:600px;text-align:center;font-size:15px;color:var(--muted);line-height:1.3}
.mkt .btn{left:468px;top:828px;width:264px;height:56px}

/* services */
.svc{top:1619px;height:754px;background:var(--blush)}
.svc .h2{left:60px;top:56px}
.svc .intro{left:60px;top:134px;font-size:17px}
.hex{position:absolute;width:98px;height:110px;background:var(--pink);clip-path:polygon(50% 0,100% 25%,100% 75%,50% 100%,0 75%,0 25%)}
.hex::after{content:"";position:absolute;left:30px;top:36px;width:38px;height:38px;border:2px solid #fff;border-radius:6px}
.svc-text{position:absolute;z-index:1}
.svc-text h3{font-size:19px;font-weight:500;line-height:1.2;margin-bottom:6px}
.svc-text ul{padding-left:14px;font-size:15px;color:var(--muted);line-height:1.25}
.col1{left:173px;width:205px}
.col2{left:512px;width:260px}
.col3{left:913px;width:230px}
.svc .ready{left:300px;top:596px;width:600px;text-align:center;font-size:15px}
.svc .btn{left:412px;top:638px;width:376px;height:56px}

/* about */
.about{top:2373px;height:647px;background:#fff}
.about-photo{left:0;top:0;width:557px;height:647px;background:radial-gradient(ellipse at 45% 55%,#5fa0e6 0%,#c8a6e8 45%,#f8e1ee 70%,#fff 100%)}
.about .h2{left:600px;top:58px}
.about .txt{left:600px;width:510px}
.about h4{font-size:19px;font-weight:600}
.about .small{font-size:15px;color:var(--muted);line-height:1.25}
.about .btn{left:600px;top:532px;width:188px;height:54px}

/* testimonials */
.tst{top:3020px;height:673px;background:var(--blush)}
.tst .h2{left:60px;top:70px}
.tst .intro{left:62px;top:150px;font-size:17px}
.quote-mark{left:570px;top:222px;font-size:110px;font-weight:700;color:var(--pink);line-height:1}
.tst .body{left:220px;top:286px;width:760px;text-align:center;font-size:15.5px;line-height:1.2}
.tst .body p{margin-bottom:20px}
.tst .who{left:0;top:530px;width:1200px;text-align:center}
.tst .who b{font-size:18px;font-weight:600;display:block}
.tst .who span{font-size:15px;color:var(--muted)}
.dots{left:550px;top:594px;display:flex;gap:22px}
.dots i{width:20px;height:20px;border-radius:50%;border:2px solid var(--purple)}
.dots i.on{background:var(--purple)}

/* contact */
.contact{top:3693px;height:578px;background:#fff}
.contact-panel{left:594px;top:0;width:606px;height:578px;background:var(--blush-deep)}
.contact .h2{left:60px;top:70px}
.contact .lead{left:60px;top:146px;width:410px;font-size:17px;line-height:1.35}
.contact .form-h{left:60px;top:262px;font-size:19px;font-weight:600}
.contact .form-n{left:60px;top:302px;width:400px;font-size:15px;color:var(--muted);line-height:1.25}
.contact-panel h4{position:absolute;left:67px;top:78px;font-size:19px;font-weight:600}
.field{position:absolute;background:transparent;border:1.5px solid #b8a0c3;padding:14px 18px;font-size:15px;color:#8a6f8f}
.contact-panel .btn{left:67px;top:461px;width:261px;height:55px}

/* footer */
.foot{top:4271px;height:207px;background:#fff}
.foot .brand{left:60px;top:28px;font-size:24px}
.foot .ack{left:60px;top:84px;width:320px;font-size:11px;line-height:1.5}
.foot h5{position:absolute;font-size:14px;font-weight:600}
.cinfo{position:absolute;left:587px;display:flex;align-items:center;gap:12px;font-size:12px;color:var(--purple)}
.cinfo i{width:24px;height:24px;background:var(--pink);border-radius:5px;display:flex;align-items:center;justify-content:center}
.qlinks{left:938px;top:72px;font-size:11px;line-height:2.15}
.bar{top:4478px;height:76px;background:var(--pink);color:#fff;text-align:center;font-size:11px;line-height:76px}
</style>
</head>
<body>

<header class="sec nav">
  <div class="brand"><span class="brand-mark"></span>Tall Pine</div>
  <nav class="menu"><span class="on">HOME</span><span>ABOUT</span><span>HOW WE HELP</span><span>FEES</span></nav>
  <a class="btn btn-outline">Get In Touch</a>
</header>

<section class="sec hero">
  <div class="abs hero-photo" role="img" aria-label="Portrait of the founder in a blue blazer, resting chin on hand"></div>
  <h1 class="abs">Carefully <span class="accent">Considered</span><br><b>Expertly <span class="accent">Crafted</span></b></h1>
  <p class="abs sub">Strategic Communication and Reputation Management Specialist</p>
  <p class="abs lead">When you have a message to deliver, a story to tell, something to say that you need your stakeholders to hear loud and clear…</p>
  <p class="abs can"><span class="accent">Tall Pine</span> can help.</p>
  <a class="btn">Get In Touch</a>
</section>

<section class="sec mkt">
  <h2 class="abs h2">Marketing <span class="accent">solution<br>to your business</span></h2>
  <p class="abs intro">In business, messaging always matters…</p>
  <div class="card" style="left:60px;top:238px"><div class="ico"></div><h3>Build Authority</h3><p>Do you have a message to share that will build trust with the audiences that drive your revenue?</p></div>
  <div class="card" style="left:426px;top:238px"><div class="ico"></div><h3>Promote Your Offers</h3><p>Perhaps you need help promoting your people or services, or ensure they are known by a wider audience?</p></div>
  <div class="card" style="left:793px;top:238px"><div class="ico"></div><h3>Craft a Powerful Narrative</h3><p>Is there a narrative to be carefully devised and managed to prevent the erosion of trust amongst your important stakeholders, either internal or external?</p></div>
  <div class="card" style="left:60px;top:493px"><div class="ico"></div><h3>Manage Crisis</h3><p>Is there a narrative to be carefully devised and managed to prevent the erosion of trust amongst your important stakeholders, either internal or external?</p></div>
  <div class="card" style="left:426px;top:493px"><div class="ico"></div><h3>Handle Media Requests</h3><p>Has the media come knocking and you're not sure what to say?</p></div>
  <div class="card" style="left:793px;top:493px"><div class="ico"></div><h3>Better Website</h3><p>Do you need a website that is cohesive and sharp?</p></div>
  <p class="abs close">We'd love to talk about how we can help shape your narrative, overcome your communications challenges, and support you to say what needs to be said.</p>
  <a class="btn">Get In Touch</a>
</section>

<section class="sec svc">
  <h2 class="abs h2">Wide <span class="accent">range of services</span></h2>
  <p class="abs intro">We help you communicate with clarity &amp; impact.</p>
  <div class="hex" style="left:60px;top:219px"></div>
  <div class="hex" style="left:399px;top:219px"></div>
  <div class="hex" style="left:799px;top:219px"></div>
  <div class="hex" style="left:60px;top:409px"></div>
  <div class="hex" style="left:399px;top:409px"></div>
  <div class="hex" style="left:799px;top:409px"></div>
  <div class="svc-text col1" style="top:216px"><h3>Media Relations &amp; Strategy</h3><ul><li>Media strategy, liaison, management, and execution</li></ul></div>
  <div class="svc-text col2" style="top:216px"><h3>Crisis &amp; Reputation Management</h3><ul><li>Expertise in post-cyber incident communications</li><li>Crisis and issues management</li></ul></div>
  <div class="svc-text col3" style="top:216px"><h3>Corporate &amp; Internal Communication</h3><ul><li>Corporate communication strategy</li><li>Executive and internal communication</li></ul></div>
  <div class="svc-text col1" style="top:407px"><h3>Public Relations &amp; Brand Building</h3><ul><li>B2B public relations</li><li>Brand building and storytelling</li></ul></div>
  <div class="svc-text col2" style="top:407px"><h3>Strategic Communication Services</h3><ul><li>Communications strategy and counsel</li><li>Change communications</li><li>Narrative development</li></ul></div>
  <div class="svc-text col3" style="top:407px;width:170px"><h3>Content Creation</h3><ul><li>Copywriting in all its forms</li></ul></div>
  <p class="abs ready">Ready to elevate your communications? Let's make it happen.</p>
  <a class="btn">Discover How We Can Help</a>
</section>

<section class="sec about">
  <div class="abs about-photo" role="img" aria-label="Smiling portrait of the founder in a blue blazer, leaning on folded arms"></div>
  <h2 class="abs h2">About <span class="accent">Tall Pine</span></h2>
  <p class="abs txt" style="top:142px;font-size:17px;line-height:1.35">We help businesses of all sizes communicate with clarity and impact.</p>
  <h4 class="abs txt" style="top:210px">Who We Are:</h4>
  <p class="abs txt small" style="top:252px">Tall Pine is led by Claire Holloway, a communications expert with 20 years of experience. We specialize in shaping strategic narratives, managing reputational challenges, and delivering results-driven communication.</p>
  <h4 class="abs txt" style="top:350px">Meet Claire:</h4>
  <p class="abs txt small" style="top:396px">Claire has worked in industries like mining, aviation, and insurance, holding senior roles including Director of Communication. With a journalism background, she brings a unique edge to media relations, PR, and crisis management.</p>
  <a class="btn btn-outline">Learn More</a>
</section>

<section class="sec tst">
  <h2 class="abs h2">Our <span class="accent">clients say this …</span></h2>
  <p class="abs intro">Discover what our clients say about us "<b>Tall Pine</b>".</p>
  <div class="abs quote-mark">&#8220;</div>
  <div class="abs body">
    <p>We engaged Claire Holloway of Tall Pine to assist with an announcement about leadership changes and growth ambitions. Crafting the right message for our market was a challenge; strategically we were hoping for some industry media coverage. Claire did what Claire said she would and successfully secured this coverage to meet our objectives.</p>
    <p>Claire made the entire process quick and seamless. She took the time to ask insightful questions to truly understand the message we wanted to convey. The end result was exactly what we needed. Our press release was picked up by the targeted publications, and the response from the market was overwhelmingly positive.</p>
    <p>We are extremely impressed with Claire's media counsel and highly recommend Tall Pine to anyone in need of professional, impactful media relations services and or/ great copywriting.</p>
  </div>
  <div class="abs who"><b>Marcus Kell</b><span>Harbour Underwriting</span></div>
  <div class="abs dots"><i class="on"></i><i></i><i></i></div>
</section>

<section class="sec contact">
  <div class="abs contact-panel">
    <h4>We'll get back to you as soon as possible.</h4>
    <div class="field" style="left:67px;top:148px;width:224px;height:50px">Your Name*</div>
    <div class="field" style="left:314px;top:148px;width:225px;height:50px">Your Email*</div>
    <div class="field" style="left:67px;top:222px;width:224px;height:50px">Your Phone Number*</div>
    <div class="field" style="left:314px;top:222px;width:225px;height:50px">Company Name</div>
    <div class="field" style="left:67px;top:297px;width:472px;height:127px">How can we help?</div>
    <a class="btn">Send Message</a>
  </div>
  <h2 class="abs h2">Let's <span class="accent">Get in Touch</span></h2>
  <p class="abs lead">We'd love to hear from you! Whether you're looking to elevate your communications, manage a critical issue, or simply explore how we can support your business, reach out today.</p>
  <p class="abs form-h">Fill Out the Form:</p>
  <p class="abs form-n">Please provide as much detail as possible so we can best assist you.</p>
</section>

<footer class="sec foot">
  <div class="brand"><span class="brand-mark"></span>Tall Pine</div>
  <p class="abs ack">Tall Pine acknowledges the Traditional Owners of Country throughout the land we call Australia. In particular, we pay our respect to the Cammeraygal people of the Eora nation whose Country our business operates from. We recognize all First Nations peoples' continuing connection to land, waters, and culture and pay our respects to their Elders past and present.</p>
  <h5 style="left:587px;top:36px">Contact Information</h5>
  <div class="cinfo" style="top:76px"><i><svg width="14" height="14" viewBox="0 0 24 24"><path fill="#fff" d="M6.6 10.8a15 15 0 0 0 6.6 6.6l2.2-2.2a1 1 0 0 1 1-.25 11.4 11.4 0 0 0 3.6.57 1 1 0 0 1 1 1V20a1 1 0 0 1-1 1A17 17 0 0 1 3 4a1 1 0 0 1 1-1h3.5a1 1 0 0 1 1 1c0 1.25.2 2.45.57 3.57a1 1 0 0 1-.25 1z"/></svg></i>+61 400 555 218</div>
  <div class="cinfo" style="top:110px"><i><svg width="14" height="12" viewBox="0 0 24 18"><rect x="1" y="1" width="22" height="16" rx="2" fill="none" stroke="#fff" stroke-width="2"/><path d="M2 2l10 8 10-8" fill="none" stroke="#fff" stroke-width="2"/></svg></i>claire.holloway@tallpine.com.au</div>
  <div class="cinfo" style="top:144px"><i></i>Claire Holloway | Profile</div>
  <h5 style="left:938px;top:36px">Quick Links</h5>
  <div class="abs qlinks">Home<br>About<br>How We Help<br>Fees</div>
</footer>

<div class="sec bar">© 2024 Tall Pine. All Rights Reserved.</div>

</body>
</html>
```